Larkspur Ridge Management - Business Cards

I need business cards. My current logo was designed by a designer at this site and I very much like and am happy with the results. I would like a business card that is trendy, unique, current yet professional. I deal with high net worth clients daily

Target Market(s)

Out of state investors looking to get into the rental market in Ohio

Industry/Entity Type

Property Management, Consulting

Contact Information for Business Card

Name, Title (Chief Financial Officer) office phone number (555) 817-3094 website address larkridgemgmt.example

Font styles to use
Sans Serif

Colors
0054AA
0677BA
7BADD7
CADEEF
E8F1F8
0094D4
00A9DD
6FCCEA
C7EBF8
E9F6FB
00AB8E
00BBA5
67D7C9
C6EFE9
E9F9F6

```html
<!DOCTYPE html>
<html lang="en">
<head>
<meta charset="utf-8">
<title>Larkspur Ridge Management – Business Cards</title>
<link href="https://fonts.googleapis.com/css2?family=Montserrat:wght@700;800&family=Open+Sans:ital,wght@0,400;1,400&display=swap" rel="stylesheet">
<style>
  :root{
    --navy:#1e2a4c;
    --red:#c8202b;
    --white:#ffffff;
    --ink:#3b3b3b;
    --faint:#f1f1f3;
    --stage:#e6e7ea;
  }
  *{margin:0;padding:0;box-sizing:border-box}
  html,body{width:1200px;height:963px;overflow:hidden;background:var(--stage)}
  .sheet{position:relative;width:1200px;height:963px}
  .card{position:absolute;left:250px;width:700px;height:400px;border-radius:22px;overflow:hidden;box-shadow:0 10px 30px rgba(0,0,0,.18)}
  .card--front{top:50px;background:var(--white)}
  .card--back{top:513px;background:var(--navy)}

  .front-mark{position:absolute;left:0;bottom:0;width:100%;height:100%}
  .brand{position:absolute;font-family:"Montserrat",sans-serif;font-weight:800;color:var(--navy);text-transform:uppercase;line-height:1.05;display:flex;align-items:center;gap:14px}
  .brand__box{width:22px;height:22px;background:var(--red);flex:none}
  .card--front .brand{left:60px;top:70px;font-size:26px;width:330px}
  .card--back .brand{left:0;right:0;top:0;bottom:0;justify-content:center;color:var(--white);font-size:34px;text-align:center}

  .contact{position:absolute;left:60px;top:235px;font-family:"Open Sans",sans-serif;font-size:20px;color:var(--ink);list-style:none}
  .contact li{display:flex;align-items:center;gap:10px;margin-bottom:8px}
  .contact svg{width:18px;height:18px;flex:none}

  .person{position:absolute;right:70px;top:150px;text-align:right}
  .person__name{font-family:"Montserrat",sans-serif;font-weight:700;font-size:24px;color:var(--red);letter-spacing:.5px;text-transform:uppercase}
  .person__title{font-family:"Open Sans",sans-serif;font-style:italic;font-size:19px;color:var(--ink);margin-top:2px}
  .accent{position:absolute;right:0;top:165px;width:40px;height:40px;background:var(--red)}
</style>
</head>
<body>
<main class="sheet">
  <section class="card card--front">
    <svg class="front-mark" viewBox="0 0 700 400" preserveAspectRatio="none" aria-hidden="true">
      <rect x="330" y="230" width="260" height="170" fill="var(--faint)"/>
      <polygon points="0,330 260,382 260,400 0,400" fill="var(--red)"/>
      <polygon points="262,386 700,360 700,400 262,400" fill="var(--navy)"/>
      <polygon points="255,381 268,383 268,400 255,400" fill="var(--white)"/>
    </svg>
    <div class="brand"><span class="brand__box"></span><span>Larkspur Ridge Management</span></div>
    <ul class="contact">
      <li><svg viewBox="0 0 24 24"><path fill="var(--red)" d="M6.6 10.8a15 15 0 0 0 6.6 6.6l2.2-2.2c.3-.3.7-.4 1-.2 1.1.4 2.3.6 3.6.6.6 0 1 .4 1 1V20c0 .6-.4 1-1 1A17 17 0 0 1 3 4c0-.6.4-1 1-1h3.5c.6 0 1 .4 1 1 0 1.3.2 2.5.6 3.6.1.3 0 .7-.2 1z"/></svg>(555) 817-3094</li>
      <li><svg viewBox="0 0 24 24"><circle cx="12" cy="12" r="10" fill="var(--red)"/><path d="M2 12h20M12 2c3 3 3 17 0 20M12 2c-3 3-3 17 0 20" stroke="var(--white)" stroke-width="1.5" fill="none"/></svg>www.larkridgemgmt.example</li>
    </ul>
    <div class="person">
      <p class="person__name">Daniel Harper</p>
      <p class="person__title">Chief Financial Officer</p>
    </div>
    <div class="accent"></div>
  </section>

  <section class="card card--back">
    <div class="brand"><span class="brand__box"></span><span>Larkspur Ridge<br>Management</span></div>
  </section>
</main>
</body>
</html>
```